Wine Label for established niche winery

Ashgrove Ridge Vineyard (www.ashgroveridgevineyard.example) is a well-respected winery in Vermont. We are a family business; a pioneer in Vermont wine; consistent quality; a winery that grows all its own grapes (a rarity in Vermont, where so many grapes are purchased from out of state).

We're launching a new line of wines, less serious and less formal than our original collection of dry wines. One of these new wines is Emberfall, a delicate and slightly sweet rosé with notes of rose and cherry wood.

Emberfall will be bottled in a flint bordeaux bottle with a silver capsule. The label will be printed on Parlin 7, and so the design we're looking for will have a lot of white space.

We're looking for a clean, simple, accessible design.

One option for an image- tree rings in cross section- is attached. You can use that image, use something similar of your own design, or draw something else entirely that fits the "Emberfall" name.

Also optional: a mountain profile that is used in some of our other labels (see attached).

Target Market(s)

Beginning wine drinkers, sweet wine drinkers, folks who are often intimidated by wine choices

Industry/Entity Type

Business

Requirements
Must have
• Must have the following text:
Ashgrove Ridge Vineyard (goudy modern- see attached) at the bottom of the label
Vermont
Emberfall
rosé wine
ALC. 10.4% BY VOL.

Must have one main image.

Must be no larger than 3.5" wide by 4.25" tall.

```html
<!DOCTYPE html>
<html lang="en">
<head>
<meta charset="utf-8">
<title>Emberfall rosé wine label – Ashgrove Ridge Vineyard</title>
<link rel="stylesheet" href="https://fonts.googleapis.com/css2?family=Sorts+Mill+Goudy:ital@0;1&family=Crimson+Text:ital@0;1&display=swap">
<style>
  :root {
    --backdrop: #e4e4e4;
    --paper: #ffffff;
    --ink: #111111;
    --ring-dark: #1c1c1c;
    --ring-mid: #8a8a8a;
    --ring-light: #f2f2f2;
  }
  * { margin: 0; padding: 0; box-sizing: border-box; }
  html, body {
    width: 1200px;
    height: 900px;
    overflow: hidden;
    background: var(--backdrop);
  }
  .canvas {
    position: relative;
    width: 1200px;
    height: 900px;
  }
  .label {
    position: absolute;
    left: 281px;
    top: 41px;
    width: 638px;
    height: 817px;
    background: var(--paper);
    box-shadow: 0 4px 14px rgba(0,0,0,0.25);
    color: var(--ink);
    text-align: center;
  }
  .label__frame {
    position: absolute;
    left: 19px;
    top: 35px;
    width: 600px;
    height: 745px;
    border: 2px solid var(--ink);
  }
  .label__line {
    position: absolute;
    left: 0;
    width: 100%;
    line-height: 1;
  }
  .wine-name {
    top: 58px;
    font-family: "Sorts Mill Goudy", Georgia, serif;
    font-size: 56px;
    font-variant: small-caps;
    letter-spacing: 1px;
  }
  .wine-type {
    top: 109px;
    font-family: "Sorts Mill Goudy", Georgia, serif;
    font-size: 28px;
  }
  .vintage {
    top: 159px;
    font-family: "Sorts Mill Goudy", Georgia, serif;
    font-style: italic;
    font-size: 23px;
  }
  .main-image {
    position: absolute;
    left: 131px;
    top: 203px;
    width: 372px;
    height: 372px;
    border-radius: 50%;
    background: radial-gradient(circle at 50% 48%, var(--ring-dark) 0%, var(--ring-mid) 30%, var(--ring-light) 60%, var(--ring-mid) 88%, var(--ring-dark) 100%);
  }
  .winery-name {
    top: 619px;
    font-family: "Sorts Mill Goudy", Georgia, serif;
    font-size: 60px;
    font-variant: small-caps;
    letter-spacing: 1px;
  }
  .winery-sub {
    top: 702px;
    font-family: "Sorts Mill Goudy", Georgia, serif;
    font-size: 25px;
    letter-spacing: 6px;
  }
  .alcohol {
    top: 739px;
    font-family: "Sorts Mill Goudy", Georgia, serif;
    font-style: italic;
    font-size: 15px;
  }
  .tagline {
    top: 766px;
    left: 50%;
    width: auto;
    transform: translateX(-50%);
    padding: 0 10px;
    background: var(--paper);
    white-space: nowrap;
    font-family: "Crimson Text", Georgia, serif;
    font-style: italic;
    font-size: 27px;
  }
</style>
</head>
<body>
  <main class="canvas">
    <article class="label">
      <div class="label__frame"></div>
      <h1 class="label__line wine-name">Emberfall</h1>
      <p class="label__line wine-type">rosé wine</p>
      <p class="label__line vintage">2013 &nbsp;|&nbsp; Vermont</p>
      <div class="main-image" role="img" aria-label="Tree rings in cross section, black and white illustration"></div>
      <h2 class="label__line winery-name">Ashgrove Ridge</h2>
      <p class="label__line winery-sub">VINEYARD</p>
      <p class="label__line alcohol">ALC. 10.4% BY VOL.</p>
      <p class="label__line tagline">Grown, produced, and bottled at our vineyard</p>
    </article>
  </main>
</body>
</html>
```